Stationery for a recruitment agency

We need a logo, letterhead and business card design that will represent our 28 year old recruitment agency that was started by us in 1989 here in Perth (Australia). We target professional companies that want us to do their sourcing and screening of candidates.

Primarily our clients like to use agencies as we have greater access to candidates than they do. Our imagery needs to reflect strength and that we are serious about recruiting and systems, and that we can meet their people supply needs both now and into the future.

Once we place a person into a job we also help manage their performance as we do Performance Appraisals and link the goals of the company to the KPI's (Key Performance Indicators) of the individual.

Target Market(s)

Corporate companies with 50+ employees

Industry/Entity Type

Recruitment

Font styles to use
Serif
Sans Serif

Colors

Designer to choose colors to be used in the design.

Requirements
Must have
• Our business name is Harbourline Staffing and must be used in the logo
Nice to have
• Having been around since 1989 is a pretty big thing in such a competitive business.

```html
<!DOCTYPE html>
<html lang="en">
<head>
<meta charset="utf-8">
<title>Harbourline Staffing – Letterhead</title>
<link href="https://fonts.googleapis.com/css2?family=Lato:wght@400;700&family=Cinzel:wght@400;500&family=Dancing+Script:wght@500&display=swap" rel="stylesheet">
<style>
  :root {
    --backdrop: #d9d9d9;
    --paper: #fbfbfb;
    --brand-blue: #0d4a9c;
    --ink: #1f1f1f;
    --grey-line: #8a8a8a;
    --watermark: rgba(0,0,0,0.045);
  }
  * { margin: 0; padding: 0; box-sizing: border-box; }
  html, body { width: 1200px; height: 1048px; overflow: hidden; background: var(--backdrop); }
  .letterhead {
    position: absolute; left: 246px; top: 24px; width: 707px; height: 1000px;
    background: var(--paper); overflow: hidden;
    font-family: "Lato", Arial, sans-serif; color: var(--ink);
    box-shadow: 0 4px 14px rgba(0,0,0,0.18);
  }
  .brand-mark {
    position: absolute; left: 59px; top: 76px;
    display: flex; align-items: center; gap: 10px;
    font-family: "Lato", Arial, sans-serif; font-weight: 700; font-size: 24px;
    color: var(--brand-blue); letter-spacing: 0.5px;
  }
  .brand-mark .brand-square { width: 22px; height: 22px; background: var(--brand-blue); }
  .sender {
    position: absolute; right: 56px; top: 76px; text-align: right;
    font-size: 10.5px; line-height: 13px; font-style: normal;
  }
  .sender .sender-name {
    font-family: "Cinzel", Georgia, serif; font-size: 13.5px; color: var(--brand-blue);
    line-height: 16px; letter-spacing: 0.4px;
  }
  .recipient {
    position: absolute; left: 56px; top: 262px; font-size: 14px; line-height: 18px;
  }
  .salutation { position: absolute; left: 56px; top: 360px; font-size: 16px; }
  .letter-body {
    position: absolute; left: 56px; top: 400px; width: 592px;
    font-size: 12.1px; line-height: 15.4px; text-align: justify;
  }
  .letter-body p { margin-bottom: 15px; }
  .letter-body p.tight { margin-bottom: 10px; }
  .closing { position: absolute; left: 56px; top: 710px; font-size: 12.5px; }
  .signer {
    position: absolute; left: 56px; top: 726px;
    font-family: "Dancing Script", cursive; font-size: 26px; color: var(--brand-blue);
  }
  .watermark {
    position: absolute; left: 0; right: 0; top: 840px; text-align: center;
    white-space: nowrap; line-height: 1;
    font-family: "Cinzel", Georgia, serif; font-size: 76px; color: var(--watermark);
  }
  .footer-band { position: absolute; left: 0; bottom: 0; width: 707px; height: 38px; }
  .footer-contacts {
    position: absolute; left: 0; right: 0; bottom: 10px;
    display: flex; justify-content: center; gap: 14px;
    font-size: 10.5px; color: #fff;
  }
  .footer-contacts span { display: inline-flex; align-items: center; gap: 5px; }
  .footer-contacts svg { width: 10px; height: 10px; }
</style>
</head>
<body>
<main class="letterhead">
  <div class="brand-mark"><span class="brand-square"></span>Harbourline Staffing</div>

  <address class="sender">
    <div class="sender-name">Harbourline Staffing</div>
    <div>27 Wharfside Terrace Level 3</div>
    <div>Fremantle, WA 6160</div>
  </address>

  <div class="recipient">
    <div>Mr/s</div>
    <div>First &amp; Last name</div>
    <div>Company name</div>
    <div>Address</div>
  </div>

  <div class="salutation">Dear Sir</div>

  <div class="letter-body">
    <p>Lorem Ipsum is simply dummy text of the printing and typesetting industry. Lorem Ipsum has been the industry's standard dummy text ever since the 1500s, when an unknown printer took a galley of type and scrambled it to make a type specimen book. It was popularised in the 1960s with the release of Stenmark sheets containing Lorem Ipsum passages, and more recently with desktop publishing software like Pagewell</p>
    <p>It is a long established fact that a reader will be distracted by the readable content of a page when looking at its layout. The point of using Lorem Ipsum is that it has a more-or-less normal distribution of letters, as opposed to using 'Content here, content here', making it look like readable English. It is a long established fact etters, as opposed to using that a reader will be etters, as opposed to using distracted by the readable</p>
    <p class="tight">The point of using Lorem Ipsum is that it has a more-or-less normal distribution of letters, as opposed to using 'Content here, content here', making it look like readable English. page editors now use Lorem Ipsum as their default model text, and a search for 'lorem ipsum' will uncover many web sites still in their infancy. Various versions have evolved over the years, sometimes by accident, sometimes on purpose (injected humour and the like. English. page editors now use Lorem Ipsum as their default model text, and a search for 'lorem ipsum'</p>
    <p>It is a long established fact that a reader will be distracted by the readable content of a page when looking at its layout. The point of using Lorem Ipsum is that it has a more-or-less normal distribution of letters, as opposed to using 'Content here, content here', making it look like readable English.</p>
  </div>

  <div class="closing">Warm regards</div>
  <div class="signer">Owen</div>

  <div class="watermark" aria-hidden="true">HARBOURLINE</div>

  <svg class="footer-band" viewBox="0 0 707 38" aria-hidden="true">
    <path d="M0 11 H95 L101 17 H0 Z" fill="var(--grey-line)"/>
    <path d="M707 11 H590 L584 17 H707 Z" fill="var(--grey-line)"/>
    <path d="M0 28 H707 V38 H0 Z" fill="var(--brand-blue)"/>
    <path d="M102 28 C108 28 108 2 122 2 H566 C580 2 580 28 586 28 Z" fill="var(--brand-blue)"/>
  </svg>
  <div class="footer-contacts">
    <span><svg viewBox="0 0 10 10"><circle cx="5" cy="5" r="4.3" fill="none" stroke="#fff" stroke-width="0.9"/><path d="M3.4 2.8 L4.3 3.7 3.8 4.4 C4.2 5.2 4.8 5.8 5.6 6.2 L6.3 5.7 7.2 6.6 6.6 7.3 C4.8 7 3 5.2 2.7 3.4 Z" fill="#fff"/></svg>08 9430 5172</span>
    <span><svg viewBox="0 0 10 10"><rect x="1" y="2.5" width="8" height="5.5" fill="#fff"/><path d="M1 2.5 L5 5.6 9 2.5" fill="none" stroke="var(--brand-blue)" stroke-width="0.9"/></svg>info@harbourlinestaffing.com</span>
    <span><svg viewBox="0 0 10 10"><circle cx="5" cy="5" r="4.3" fill="#fff"/><path d="M0.7 5 H9.3 M5 0.7 C2.8 3 2.8 7 5 9.3 M5 0.7 C7.2 3 7.2 7 5 9.3" fill="none" stroke="var(--brand-blue)" stroke-width="0.6"/></svg>www.harbourlinestaffing.com</span>
  </div>
</main>
</body>
</html>
```